New company website for Redfern Hollow Building Company

We're looking to build a new company website that customers can use to contact us, get quotes, view past projects (renovations, additions, new construction, etc.), & learn more about our business. We want to use Pressfield for our website and have already purchased the Divi theme (by Quillmark Studio). Using that theme isn't required but we already have several examples of websites that we want to model our site after that use this theme. The "look" we're after is simple, light, & clean.

Target Market(s)

Residential remodeling, renovations, and new construction.

Industry/Entity Type

Residential Construction

Coding

Coded - Design and coding required

Number of Pages Required

5+ page

Font styles to use
Sans Serif

Colors
33a6d7
aaaaaa

Requirements
Must have
• We require the website to be coded using the Divi theme. We'll be upgrading the project to include this today or tomorrow.
• The navigation bar should be static & remain at the top of the page. When scrolling we'd like the logo & info in the nav bar to size down. Here's an example of a site that does this: https://tovamerihomes.example/
Nice to have
• In the gallery with pictures of our finished product/jobs, when you mouse over the image, we'd like there to be additional info that shows up. For example, look at this gallery: https://tovamerihomes.example/projectcategories/kitchens/ We'll add a name/location of the job like: "Garvey kitchen - Apex, N.C."
• If you go to this website: https://plinvorworks.example/ and scroll down to the pictures, we like how the picture moves and is interactive.

```html
<!DOCTYPE html>
<html lang="en">
<head>
<meta charset="utf-8">
<title>Redfern Hollow Building Company</title>
<link href="https://fonts.googleapis.com/css2?family=Josefin+Sans:wght@400;600;700&family=Raleway:wght@400;500;600&display=swap" rel="stylesheet">
<style>
:root{
  --accent:#33a6d7;
  --grey:#aaaaaa;
  --grey-dark:#777777;
  --text:#666666;
  --light:#f2f2f2;
  --band:#e6e6e6;
  --ink:#222222;
  --admin:#23282d;
}
*{box-sizing:border-box;margin:0;padding:0}
html,body{width:1200px;height:3291px;overflow:hidden}
body{position:relative;background:#fff;font-family:"Raleway",sans-serif;color:var(--text)}
.abs{position:absolute}
.admin-bar{left:0;top:0;width:1200px;height:28px;background:var(--admin);color:#eee;font-size:11px;display:flex;align-items:center;padding:0 10px;gap:22px}
.admin-bar .dot{width:14px;height:14px;border-radius:50%;background:#999;display:inline-block;vertical-align:middle;margin-right:5px}
.admin-bar .right{margin-left:auto}
.site-header{left:0;top:28px;width:1200px;height:117px;background:#fff;border-bottom:1px solid #ddd}
.header-phone{right:28px;top:10px;font-size:30px;color:var(--ink);display:flex;align-items:center;gap:10px;letter-spacing:1px}
.logo{font-family:"Josefin Sans",sans-serif;font-weight:700;color:var(--grey-dark);text-transform:uppercase;line-height:1}
.site-header .logo{left:30px;top:54px;font-size:19px;letter-spacing:1px}
.main-nav{right:28px;top:74px;display:flex;gap:22px;font-family:"Josefin Sans",sans-serif;font-size:17px;font-weight:600;color:var(--accent);text-transform:uppercase}
.photo{display:block}
.hero{left:0;top:145px;width:1200px;height:455px;background:linear-gradient(180deg,#cfd3d4 0%,#ecedeb 45%,#b9b2a8 80%,#8c7f72 100%)}
.section-title{font-family:"Josefin Sans",sans-serif;font-weight:600;color:var(--accent);text-transform:uppercase;letter-spacing:1px}
.intro-title{left:44px;top:648px;width:680px;font-size:28px;line-height:1.05}
.intro-text{left:44px;top:718px;width:720px;font-size:12.5px;line-height:19px;color:#8a8a8a}
.btn-outline{border:2px solid var(--accent);color:var(--accent);font-size:13px;text-transform:uppercase;letter-spacing:1px;display:flex;align-items:center;justify-content:center;gap:10px}
.intro-btn{left:340px;top:851px;width:132px;height:44px}
.slider{left:812px;top:645px;width:351px;height:232px;background:linear-gradient(135deg,#7a4a2e 0%,#d99a5e 45%,#efe4d2 70%,#8b5a3a 100%)}
.slider-dots{left:965px;top:894px;display:flex;gap:6px}
.slider-dots span{width:6px;height:6px;border-radius:50%;background:#ccc}
.slider-dots span:first-child{background:var(--accent)}
.divider{left:44px;top:959px;width:1112px;height:1px;background:#e6e6e6}
.process-title{left:0;top:1012px;width:1200px;text-align:center;font-size:22px}
.process-img{left:123px;top:1075px;width:447px;height:301px;background:linear-gradient(135deg,#e9ecee 0%,#c8ced3 50%,#9aa3aa 100%);border:4px solid #f0f0f0}
.process-list{left:647px;top:1068px;list-style:none}
.process-list li{height:38.4px;display:flex;align-items:center;gap:12px;font-size:14px;color:#555}
.process-list li::before{content:"";width:12px;height:12px;border-radius:50%;background:var(--accent)}
.link-more{color:var(--accent);font-size:16px;display:flex;align-items:center;gap:16px}
.process-more{left:687px;top:1384px}
.band{left:0;width:1200px;background:var(--band)}
.tile{top:0;height:100%;display:flex;align-items:center;justify-content:center}
.tile-label{background:rgba(170,170,170,.92);color:#fff;text-transform:uppercase;letter-spacing:1px;display:flex;align-items:center;justify-content:center}
.spec-row{left:0;top:1499px;width:1200px;height:283px}
.spec-row .tile{width:400px}
.spec-row .tile-label{width:240px;height:72px;font-size:17px}
.room-row{left:0;top:1815px;width:1200px;height:210px}
.room-row .tile{width:300px}
.room-row .tile-label{width:150px;height:50px;font-size:14px;font-weight:600;text-transform:none;letter-spacing:0}
.testimonial{left:0;top:2076px;width:1200px;height:333px;background:linear-gradient(90deg,#f4f2ef 0%,#ece6df 50%,#e6ddd3 100%)}
.quote-text{left:195px;top:2146px;width:810px;text-align:center;font-size:19px;line-height:34px;color:#555;letter-spacing:.5px}
.testimonial-more{left:544px;top:2310px}
.blog-title{left:121px;top:2440px;font-size:30px}
.blog-list{left:132px;top:2552px;width:440px;height:307px;overflow:hidden}
.blog-scroll{left:428px;top:0;width:10px;height:307px;background:#eee}
.blog-scroll::after{content:"";position:absolute;left:1px;top:0;width:8px;height:118px;background:#ccc}
.post{width:370px;margin-bottom:34px}
.post h3{font-family:"Josefin Sans",sans-serif;font-weight:400;font-size:15px;line-height:17px;color:#333;margin-bottom:14px}
.post .meta{font-size:12px;color:#666;margin-bottom:10px}
.post p{font-size:12.5px;line-height:20px;color:#555}
.post .read{color:var(--accent);font-size:12px}
.quote-box{left:627px;top:2545px;width:453px;height:404px;background:var(--grey)}
.quote-box h2{position:absolute;left:73px;top:22px;font-family:"Josefin Sans",sans-serif;font-size:21px;font-weight:600;color:#fff}
.field{position:absolute;left:75px;width:303px;height:40px;background:#fff;border:1px solid #ddd;font-size:12px;color:#888;padding:12px 10px}
.submit{position:absolute;left:77px;top:335px;width:112px;height:42px;border:2px solid #fff;color:#fff;font-size:16px;font-weight:600;display:flex;align-items:center;justify-content:center;gap:12px}
.site-footer{left:0;top:2979px;width:1200px;height:279px;background:#ececec}
.site-footer .logo{left:121px;top:47px;font-size:21px;letter-spacing:1px}
.footer-head{font-family:"Josefin Sans",sans-serif;color:var(--accent);font-size:19px}
.footer-contact{left:121px;top:117px}
.footer-address{left:121px;top:156px;font-size:12px;color:#666}
.quick{left:509px;top:42px}
.quick ul{list-style:none;margin-top:14px}
.quick li{height:34px;font-size:12px;color:#555}
.call{left:706px;top:40px}
.call h2{font-family:"Josefin Sans",sans-serif;font-size:27px;font-weight:700;color:#111;letter-spacing:1px}
.call .phone{font-size:32px;color:var(--accent);margin:6px 0 0 42px;letter-spacing:1px}
.socials{display:flex;gap:8px;margin:12px 0 0 47px}
.socials span{width:32px;height:32px;border-radius:50%;background:var(--accent)}
.bottom-bar{left:0;top:3258px;width:1200px;height:33px;background:var(--ink);color:#888;font-size:12px;display:flex;align-items:center;padding-left:121px}
.bottom-bar b{color:#aaa;font-weight:600}
</style>
</head>
<body>

<div class="abs admin-bar">
  <span><i class="dot"></i>My Sites</span><span>Redfern Service</span><span>7</span><span>0</span><span>+ New</span><span>Edit Page</span><span>Enable Visual Builder</span>
  <span class="right">Howdy, admin</span>
</div>

<header class="abs site-header">
  <div class="abs header-phone">
    <svg width="24" height="24" viewBox="0 0 24 24"><path fill="#33a6d7" d="M6.6 10.8a15 15 0 0 0 6.6 6.6l2.2-2.2c.3-.3.7-.4 1-.2 1.1.4 2.3.6 3.6.6.6 0 1 .4 1 1V20c0 .6-.4 1-1 1A17 17 0 0 1 3 4c0-.6.4-1 1-1h3.5c.6 0 1 .4 1 1 0 1.3.2 2.5.6 3.6.1.3 0 .7-.2 1z"/></svg>
    123.456.7890
  </div>
  <div class="abs logo">Redfern Hollow<br>Building Company</div>
  <nav class="abs main-nav"><span>Getting Started</span><span>Who We Are</span><span>Specialties</span><span>Portfolio</span><span>Contact Us</span></nav>
</header>

<div class="abs photo hero" role="img" aria-label="Bright white kitchen with marble island and pendant lights"></div>

<h1 class="abs section-title intro-title">We Meet and Exceed All Your Design Expectations</h1>
<p class="abs intro-text">All of our projects begin at the design phase and at Marlow Pike Interiors we offer this service at the highest level. Our award-winning interior designers will work with you to turn your project into an aesthetic, practical and successful design. Our qualified design team pride themselves on their continuing professional development and in-depth training ensuring they produce better living environments for today's lifestyle.</p>
<div class="abs btn-outline intro-btn">Read More <span>›</span></div>
<div class="abs photo slider" role="img" aria-label="Warm dining room with wooden table and chairs"></div>
<div class="abs slider-dots"><span></span><span></span><span></span></div>

<div class="abs divider"></div>

<h2 class="abs section-title process-title">Our Process</h2>
<div class="abs photo process-img" role="img" aria-label="Blueprints with drafting tools and a tablet showing a kitchen"></div>
<ul class="abs process-list">
  <li>Client Agreement</li><li>Initial Consultation</li><li>Concept</li><li>Design Development</li><li>FinalL Approval</li><li>Cabinet Making</li><li>Furnishing &amp; Decorating</li><li>Our Design Fees</li>
</ul>
<div class="abs link-more process-more">View More <span>›</span></div>

<div class="abs band" style="top:1455px;height:44px"></div>
<div class="abs spec-row">
  <div class="abs tile" style="left:0;background:linear-gradient(135deg,#6b4a30,#c79a6a,#8a6a4c)" role="img" aria-label="House framing under remodel"><div class="tile-label">Remodeling</div></div>
  <div class="abs tile" style="left:400px;background:linear-gradient(180deg,#7fb6e3 0%,#cfe3f2 45%,#b0674a 70%,#6f8a3c 100%)" role="img" aria-label="Newly built brick house"><div class="tile-label">New Construction</div></div>
  <div class="abs tile" style="left:800px;background:linear-gradient(135deg,#efe9e2,#d6a275,#b36a3c)" role="img" aria-label="Hands fitting wooden floor boards"><div class="tile-label">Additions</div></div>
</div>
<div class="abs band" style="top:1782px;height:33px"></div>
<div class="abs room-row">
  <div class="abs tile" style="left:0;background:linear-gradient(90deg,#8a7a6c,#d9d7d2)" role="img" aria-label="Room before renovation"><div class="tile-label">Before</div></div>
  <div class="abs tile" style="left:300px;background:linear-gradient(135deg,#f2f2f0,#c9c7c2)" role="img" aria-label="Renovated white kitchen"><div class="tile-label">Kitchen</div></div>
  <div class="abs tile" style="left:600px;background:linear-gradient(135deg,#6a4a2c,#d8b98a,#efe6d6)" role="img" aria-label="Renovated bathroom with stone wall"><div class="tile-label">Bathroom</div></div>
  <div class="abs tile" style="left:900px;background:linear-gradient(180deg,#8fbde3 0%,#c7a07a 55%,#7a5a44 100%)" role="img" aria-label="Large renovated family house"><div class="tile-label">Whole House</div></div>
</div>
<div class="abs band" style="top:2025px;height:51px;background:#f3f3f3"></div>

<section class="abs testimonial" role="img" aria-label="Soft faded photo of a happy couple at home"></section>
<p class="abs quote-text">Thanks so much for our beautiful room you finished for us. The process was very organized and professional. We enjoyed working with you and Theo, and your quality subcontractors.<br>-Dana R.</p>
<div class="abs link-more testimonial-more">View More <span>›</span></div>

<h2 class="abs section-title blog-title">Blog</h2>
<div class="abs blog-list">
  <article class="post">
    <h3>9 Must-Have Inclusions for your Hamptons Style Kitchen</h3>
    <div class="meta">Jun 20, 2018 | Blog | 0 Comments</div>
    <p>Hamptons style kitchens make my heart skip a beat. I get a bit overcome when I walk into one. There's something so wonderful about this type of kitchen design, don't you think?</p>
    <span class="read">Read More</span>
  </article>
  <article class="post">
    <h3>The Worst Home Swap Live Reveal in History just Happened</h3>
    <div class="meta">Jun 20, 2018 | Blog | 0 Comments</div>
    <p>You see, he doesn't understand how the Home Swap Live 2018 Lena and Paul reveal – or any of the series – works. He doesn't watch</p>
  </article>
  <div class="abs blog-scroll"></div>
</div>

<form class="abs quote-box">
  <h2>Get a Quote</h2>
  <div class="field" style="top:66px">First &amp; Last Name</div>
  <div class="field" style="top:119px">Phone Number</div>
  <div class="field" style="top:173px">Email Address</div>
  <div class="field" style="top:227px">Project's Address</div>
  <div class="field" style="top:281px">Project's Zipcode</div>
  <div class="submit">Submit <span>›</span></div>
</form>

<footer class="abs site-footer">
  <div class="abs logo">Redfern Hollow<br>Building Company</div>
  <div class="abs footer-head footer-contact">Contact Us</div>
  <div class="abs footer-address">412 Alder Row, Brookmere Texas, 75000</div>
  <div class="abs quick">
    <div class="footer-head">Quick Links</div>
    <ul><li>Get Started</li><li>Who We Are</li><li>Specialties</li><li>Portfolio</li><li>Contact</li></ul>
  </div>
  <div class="abs call">
    <h2>CALL US TODAY !</h2>
    <div class="phone">123.456.7890</div>
    <div class="socials"><span></span><span></span><span></span><span></span><span></span></div>
  </div>
</footer>
<div class="abs bottom-bar">Designed by&nbsp;<b>Quillmark Studio</b>&nbsp;| Powered by&nbsp;<b>Pressfield</b></div>

</body>
</html>
```